Business card

Hi Marta,
can you please design business cards for me?
Based on your Brimvale design please go crazy (still retain a professional business-solid profile). I would like to use really stylish paper (or different paper types and special prints like partly embossed or partly glossy and contrast the glossiness with matt for instance).
Please keep in mind that I might come back to you in several months if the business requires other print material like stationary, folders, envelopes etc. It all needs to be in line and make a huge impression without going over board and still remain very solid and serious.
I know that's a lot to ask and I apologise but I am really impressed with your work so far and have no doubt that you can spin the wheels again in a great way.
Thanks bunches, Lukas
In order to punch in the right text from the outset, here is some key data:
Brimvale
Higher ground
Lukas Brander
Chief Executive Growth Partner
+41 79 583 1067
lukas.brander@brimvale.com
brimvale.com
Business
Brimvale
Higher ground
Lukas Brander
+41 79 583 1067
brimvale.com

```html
<!DOCTYPE html>
<html lang="en">
<head>
<meta charset="utf-8">
<title>Brimvale – Business Card</title>
<link rel="stylesheet" href="https://fonts.googleapis.com/css2?family=Open+Sans:ital,wght@0,300;0,400;0,700;1,400&display=swap">
<style>
  :root {
    --backdrop: #e4e2de;
    --card-dark: #161616;
    --card-mid: #202020;
    --card-light: #2a2a2a;
    --ink-white: #f4f4f4;
    --ink-grey: #a9a9a9;
  }
  * { margin: 0; padding: 0; box-sizing: border-box; }
  html, body {
    width: 1200px;
    height: 720px;
    overflow: hidden;
    background: var(--backdrop);
    font-family: "Open Sans", Arial, sans-serif;
  }
  .sheet {
    position: relative;
    width: 1200px;
    height: 720px;
    display: flex;
    align-items: center;
    justify-content: center;
    gap: 60px;
  }
  .card {
    position: relative;
    width: 520px;
    height: 310px;
    clip-path: polygon(13% 0, 87% 0, 100% 50%, 87% 100%, 13% 100%, 0 50%);
    color: var(--ink-white);
  }
  .card--front {
    background:
      linear-gradient(112deg, transparent 0 52%, rgba(255,255,255,0.04) 52% 100%),
      linear-gradient(160deg, var(--card-light) 0%, var(--card-mid) 45%, var(--card-dark) 100%);
  }
  .card--back {
    background:
      linear-gradient(90deg, var(--card-dark) 0 13%, transparent 13% 87%, var(--card-dark) 87% 100%),
      linear-gradient(160deg, var(--card-light) 0%, var(--card-mid) 50%, var(--card-dark) 100%);
  }

  /* front */
  .brand {
    position: absolute;
    left: 0; right: 0;
    top: 124px;
    text-align: center;
  }
  .brand__name {
    font-weight: 300;
    font-size: 38px;
    letter-spacing: 0.22em;
    text-transform: uppercase;
    color: var(--ink-white);
    padding-left: 0.22em;
  }
  .brand__tagline {
    margin-top: 4px;
    font-weight: 400;
    font-size: 9px;
    letter-spacing: 0.32em;
    text-transform: uppercase;
    color: var(--ink-grey);
    padding-left: 120px;
  }

  /* back */
  .contact {
    position: absolute;
    left: 120px;
    right: 60px;
    top: 82px;
    text-align: center;
  }
  .contact__name {
    font-weight: 700;
    font-size: 14px;
    letter-spacing: 0.2em;
    text-transform: uppercase;
  }
  .contact__role {
    margin-top: 6px;
    font-style: italic;
    font-size: 11px;
    color: var(--ink-grey);
  }
  .contact__lines {
    margin-top: 26px;
    font-size: 11px;
    color: var(--ink-grey);
  }
  .contact__divider {
    display: inline-block;
    width: 4px; height: 4px;
    margin: 0 8px 2px;
    border-radius: 50%;
    background: var(--ink-white);
  }
  .contact__web {
    margin-top: 10px;
    font-weight: 700;
    font-size: 12px;
    color: var(--ink-white);
  }
</style>
</head>
<body>
  <main class="sheet">
    <section class="card card--front" aria-label="Card front">
      <div class="brand">
        <div class="brand__name">Brimvale</div>
        <div class="brand__tagline">Higher ground</div>
      </div>
    </section>

    <section class="card card--back" aria-label="Card back">
      <div class="contact">
        <div class="contact__name">Lukas Brander</div>
        <div class="contact__role">Chief Executive Growth Partner</div>
        <div class="contact__lines">
          <span class="contact__phone">+41 79 583 1067</span><span class="contact__divider"></span><span class="contact__email">lukas.brander@brimvale.com</span>
        </div>
        <div class="contact__web">brimvale.com</div>
      </div>
    </section>
  </main>
</body>
</html>
```